Theater Production Company in Las Vegas

Needing a business card for a theater production company in Las Vegas. We are a full service theatrical production company specializing in Las Vegas entertainment, national
touring shows, and one-off events. From gorilla marketing teams to large scale productions... we do it,and better than anyone.

We like the feel of something hand made and organic.The final design should be creative and communicate that we specialize in theater and special events. We would like to have a design with a front and back.

Hi All,

I want to elaborate on the style of the design that we are hoping for. We are a theater production company in Las Vegas, so the competition is fierce and having a clever business card is incredibly important. 

I am attached a few concepts of a "feel" that would be nice to have conveyed in our card. We love the "worn and vintage" feel that is often seen in antique circus posters. Traditionally, the circus posters are clustered and full of copy - I want a more simplified version of that. Not so cluttered, but with that worn feel. Perhaps even having the card printed on recycled paper to give that textured feel to the visual. 

Example 1 - has a fun worn look, with stars. Some version of this for the back of the card would be fun.
Example 2 - Same things, cool worn feel. Perhaps a small star at the center of the swirl and a little softer on the "grunge".
Example 3 - Has the circus ornament but the colors are nice, not overpowering and again, has that worn feel.
Example 4 - This design isn't as "tight" and cluttered. Has some room to breathe.
Example 5 - I am really liking the look of the this and the above, especially for the back of the card. 

But just to reiterate, the front and face of the card needs to be clear and easy to read. 

Hi Designers, 

I have posted an update so you can have a clearer understanding of what we are needing. I have also increased the funding.

Thank you in advance for your help.

Brigid

Marketing

• We want to assign creative license. We are creative and hate to be limited by restrictions. Have fun!

The attached files are our logo. One of the files is a business card design that I love. Just a sample of our taste.
• We would like to incorporate: Purveyors of Performance
as our tagline. I like a vintage, worn feel to the look of designs. Just the word "purveyor" sounds vintage.

```html
<!DOCTYPE html>
<html lang="en">
<head>
<meta charset="utf-8">
<title>Velvet Lantern Productions – Business Card</title>
<link href="https://fonts.googleapis.com/css2?family=PT+Sans:wght@400;700&display=swap" rel="stylesheet">
<style>
  :root {
    --backdrop: #2b2c2e;
    --ivory: #f7f5f1;
    --ivory-shade: #e6e2dc;
    --ink: #2a2522;
    --bronze: #8a6239;
    --bronze-dark: #6a4623;
    --chocolate: #6b4727;
    --chocolate-deep: #4f3219;
    --gold: #d9b56c;
    --gold-soft: #b98f4c;
    --white: #ffffff;
  }
  * { box-sizing: border-box; margin: 0; padding: 0; }
  html, body {
    width: 1200px; height: 384px; overflow: hidden;
    background: var(--backdrop);
    font-family: "PT Sans", Arial, sans-serif;
  }
  .canvas { position: relative; width: 1200px; height: 384px; }

  .card { position: absolute; border-radius: 22px; overflow: hidden; }

  /* Front */
  .card--front {
    left: 22px; top: 30px; width: 548px; height: 312px;
    background: linear-gradient(160deg, var(--ivory) 0%, var(--ivory-shade) 55%, var(--ivory) 100%);
  }
  .front-texture {
    position: absolute; inset: 0;
    background: radial-gradient(ellipse at 70% 35%, rgba(255,255,255,.9), rgba(220,214,206,.35) 70%);
  }
  .brand-name {
    position: absolute; left: 20px; top: 95px; width: 310px;
    text-align: center; color: var(--ink);
    font-size: 38px; font-weight: 400; line-height: 1.05;
  }
  .brand-sub {
    position: absolute; left: 20px; top: 186px; width: 310px;
    text-align: center; color: var(--ink);
    font-size: 11px; letter-spacing: 11px;
  }
  .accent-rule { position: absolute; left: 0; top: 240px; }
  .address {
    position: absolute; left: 24px; top: 259px;
    color: var(--ink); font-size: 14.5px; line-height: 21px;
  }
  .name-tab {
    position: absolute; left: 333px; top: 135px; width: 215px; height: 63px;
    background: var(--bronze);
    border-radius: 16px 0 0 16px;
    padding: 12px 0 0 16px; color: var(--white);
  }
  .name-tab__name { font-size: 18px; font-weight: 700; line-height: 20px; }
  .name-tab__role { font-size: 13px; line-height: 18px; }
  .contact {
    position: absolute; left: 348px; top: 222px;
    color: var(--ink); font-size: 14.5px; line-height: 20px;
  }
  .contact__label { display: inline-block; width: 42px; }
  .contact__web { font-weight: 700; }

  /* Back */
  .card--back {
    left: 603px; top: 32px; width: 549px; height: 315px;
    background: linear-gradient(180deg, var(--chocolate-deep) 0%, var(--chocolate) 30%, var(--chocolate) 70%, var(--chocolate-deep) 100%);
  }
  .ornament-band {
    position: absolute; left: 0; width: 100%; height: 44px;
    background: linear-gradient(90deg, rgba(185,143,76,.35), rgba(217,181,108,.55), rgba(185,143,76,.35));
  }
  .ornament-band--top { top: 6px; }
  .ornament-band--bottom { bottom: 6px; }
  .tagline { position: absolute; left: 70px; top: 138px; color: var(--gold); }
  .tagline__main { font-size: 28px; letter-spacing: .5px; line-height: 30px; }
  .tagline__sub { font-size: 17px; margin-left: 44px; line-height: 24px; }
  .back-brand {
    position: absolute; left: 290px; top: 128px; width: 220px;
    text-align: center; color: var(--gold);
    font-size: 30px; line-height: 34px;
  }
</style>
</head>
<body>
<main class="canvas">
  <section class="card card--front" aria-label="Card front">
    <div class="front-texture" role="img" aria-label="Soft ivory tiled texture"></div>
    <p class="brand-name">Velvet Lantern</p>
    <p class="brand-sub">PRODUCTIONS</p>
    <svg class="accent-rule" width="225" height="10" viewBox="0 0 225 10" aria-hidden="true">
      <path d="M0 1 H212 Q222 3 222 5 Q222 7 212 9 H0 Z" fill="var(--bronze)"/>
    </svg>
    <p class="address">Lantern Row Blvd, Suite 500<br>Cityname, Countryname-2345</p>
    <div class="name-tab">
      <p class="name-tab__name">YOUR NAME</p>
      <p class="name-tab__role">Designation</p>
    </div>
    <p class="contact">
      <span class="contact__label">Cell</span> 234 567 8901<br>
      <span class="contact__label">Phone</span>234 567 8901<br>
      <span class="contact__label">Email</span> velvetlantern@site.com<br>
      <span class="contact__web">www.velvetlantern@site.com</span>
    </p>
  </section>

  <section class="card card--back" aria-label="Card back">
    <div class="ornament-band ornament-band--top" role="img" aria-label="Gold damask ornament border"></div>
    <div class="ornament-band ornament-band--bottom" role="img" aria-label="Gold damask ornament border"></div>
    <div class="tagline">
      <p class="tagline__main">PURVEYORS</p>
      <p class="tagline__sub">of Performance</p>
    </div>
    <p class="back-brand">Velvet Lantern</p>
  </section>
</main>
</body>
</html>
```